German Webagency needs fresh modern Design

Our website is 4 years old. We need an fresh modern website. All pics we used before are from customers or handmade by us. the new website should be clear with nice handling. please dont copy something from template websites. it would be great if you can surprise us with something great. its our first project here. don´t worry if i make a mistake in responding or briefing. after 20 years you can´t see the works of your own "designer" so we hope for help :-)
our existing site: www.korvanetz.de
Target Market(s)
small and middle sized companys in germany
Number of Pages Required
4 page
Font styles to use
Colors
Designer to choose colors to be used in the design.
Requirements
Must have
- Responsive (sure we code it)
- Modern and big Font ..Headlines and Slider
- innovative..if you know something new..feel free to show
Nice to have
- the site with our works/refences should look great and later easy to handle when we code it or use wp.
- we like black and grey but if you have better ideas also feel free
Should not have
- a cup of coffe..laptop.. a pencil a handwritten font
- dont copy and modify templates from know websites..bad style

```html
<!DOCTYPE html>
<html lang="en">
<head>
<meta charset="utf-8">
<title>Korvanetz – Werbeagentur</title>
<link rel="stylesheet" href="https://fonts.googleapis.com/css2?family=Poppins:wght@600;700&family=Questrial&display=swap">
<style>
:root{
  --blue:#3aa3e3;
  --blue-deep:#4a86d8;
  --purple:#7b5bc6;
  --violet:#5a2a9a;
  --ink:#111111;
  --text:#6e6e6e;
  --muted:#9a9a9a;
  --field:#f3f3f3;
  --footer:#2a2a2a;
  --white:#ffffff;
}
*{margin:0;padding:0;box-sizing:border-box}
html,body{width:1200px;height:3152px;overflow:hidden}
body{position:relative;background:var(--white);font-family:"Questrial",sans-serif;color:var(--text)}
.abs{position:absolute;z-index:1}
.bg{z-index:0}
.over{z-index:2}
.heading{font-family:"Poppins",sans-serif;font-weight:600;text-align:center}

.hero{left:0;top:0;width:1200px;height:900px;background:linear-gradient(115deg,var(--blue) 0%,var(--blue-deep) 45%,var(--purple) 100%)}
.shape{left:0;width:1200px}
.brand{left:164px;top:52px;display:flex;align-items:center;gap:10px;font-family:"Poppins",sans-serif;font-weight:700;font-size:30px;line-height:36px;color:#0f1f4a}
.brand-dot{width:16px;height:16px;border-radius:50%;background:#0f1f4a}
.nav{left:500px;top:56px;display:flex;align-items:center;font-family:"Poppins",sans-serif;font-weight:600;font-size:13px;color:var(--white)}
.nav a{color:inherit;text-decoration:none;margin-right:44px}
.nav .nav-contact{margin:0 0 0 6px;border:2px solid var(--white);padding:6px 22px;border-radius:2px}
.hero-title{left:150px;top:260px;width:900px;font-size:54px;line-height:64px;color:var(--white);font-weight:700}
.hero-text{left:210px;top:416px;width:780px;font-size:12px;line-height:19px;color:var(--white);text-align:center}
.hero-media{left:326px;top:557px;width:546px;height:315px;border-radius:14px;background:linear-gradient(135deg,#f1f1f1,#c9c9c9);padding:22px 40px 40px}
.hero-media div{width:100%;height:100%;background:linear-gradient(120deg,#e8e8e8 0%,#f6d36b 45%,#e2557a 65%,#4db6e8 85%)}

.section-title{left:0;width:1200px;font-size:46px;line-height:60px;color:var(--ink)}
.about-sub{left:0;top:1022px;width:1200px;text-align:center;font-family:"Poppins",sans-serif;font-weight:600;font-size:13px;color:var(--ink)}
.about-text{left:0;top:1060px;width:1200px;text-align:center;font-size:11.8px;line-height:19px;white-space:nowrap}
.about-text p{margin-bottom:9px}
.btn{background:var(--blue);color:var(--white);font-family:"Poppins",sans-serif;font-weight:600;font-size:11px;display:flex;align-items:center;justify-content:center;border-radius:2px;text-decoration:none}
.about-btn{left:547px;top:1235px;width:106px;height:32px}

.band{left:0;top:1260px;width:1200px;height:860px;background:linear-gradient(120deg,var(--blue) 0%,var(--blue-deep) 50%,var(--purple) 100%)}
.services-title{top:1520px;color:var(--white)}
.card{top:1619px;width:262px;height:400px;background:var(--white);padding:40px 0 0 34px;box-shadow:0 6px 18px rgba(0,0,0,.15);white-space:nowrap}
.card svg{display:block;height:36px;margin-bottom:16px}
.card h3{font-family:"Poppins",sans-serif;font-weight:600;font-size:12.5px;line-height:18px;color:var(--ink);margin-bottom:8px}
.card p{font-size:10.8px;line-height:18px;color:var(--muted);margin-bottom:14px}
.card .more{font-family:"Poppins",sans-serif;font-weight:600;font-size:10.5px;color:var(--ink)}

.refs-title{top:2060px}
.refs-sub{left:0;top:2136px;width:1200px;text-align:center;font-family:"Poppins",sans-serif;font-weight:600;font-size:12px;color:var(--ink)}
.ref{top:2209px;width:279px;height:206px;box-shadow:0 4px 14px rgba(0,0,0,.25)}

.contact{left:0;top:2541px;width:1200px;height:569px;background:linear-gradient(115deg,var(--blue) 0%,var(--blue-deep) 45%,var(--purple) 100%)}
.contact-title{top:2600px;color:var(--white)}
.form-card{left:422px;top:2715px;width:354px;height:395px;background:var(--white)}
.field{left:48px;width:257px;height:30px;background:var(--field);font-size:10.5px;line-height:14px;color:#aaa;padding:8px 10px}
.submit{left:126px;top:310px;width:102px;height:30px}

.footer{left:0;top:3110px;width:1200px;height:42px;background:var(--footer);display:flex;align-items:center;padding:0 162px;color:#cfcfcf;font-size:11px}
.social{left:508px;top:12px;display:flex;gap:10px}
.social span{width:18px;height:18px;border-radius:50%;background:#d8d8d8;display:block}
.support{left:934px;top:5px;width:104px;height:32px}
</style>
</head>
<body>

<section class="hero abs bg"></section>
<svg class="shape abs bg" style="top:420px" width="1200" height="480" viewBox="0 0 1200 480">
  <path d="M0 232 C300 170 700 130 1200 60 L1200 480 L0 480 Z" fill="var(--white)"/>
  <path d="M60 290 C250 200 700 120 1200 50" stroke="var(--blue)" stroke-width="14" fill="none" stroke-linecap="round"/>
  <path d="M0 240 C350 180 750 120 1200 62" stroke="var(--white)" stroke-width="6" fill="none"/>
</svg>

<div class="brand abs"><span class="brand-dot"></span>Korvanetz.de</div>
<nav class="nav abs">
  <a href="#">Home</a><a href="#">Dsgvo</a><a href="#">About</a><a href="#">Services</a><a href="#">Credentials</a><a href="#">Current</a>
  <a class="nav-contact" href="#">Contact</a>
</nav>
<h1 class="hero-title heading abs">Wir sorgen für bleibende Ein-<br>drücke !</h1>
<p class="hero-text abs">The numerous changes that the DSGVO brings with effect from May 25, 2018, affect every entrepreneur and website operator. There are extensive new regulations in almost all areas of data protection law. Some are relatively easy to implement, others are very complex.</p>
<div class="hero-media abs" role="img" aria-label="Laptop showing a man presenting a colourful painted light bulb"><div></div></div>

<section class="band abs bg"></section>
<svg class="shape abs bg" style="top:1250px" width="1200" height="220" viewBox="0 0 1200 220">
  <path d="M0 0 L1200 0 L1200 100 C900 200 400 200 0 14 Z" fill="var(--white)"/>
  <path d="M1060 60 C1140 90 1180 130 1200 170" stroke="var(--blue)" stroke-width="10" fill="none" stroke-linecap="round"/>
</svg>

<h2 class="section-title heading abs" style="top:938px">About Us</h2>
<p class="about-sub abs">Werbeagentur Korvanetz GmbH</p>
<div class="about-text abs">
  <p>The advertising agency Korvanetz has existed since 1998. Founded under the name NL-Netzservice, we have been successfully accompanying your projects on<br>the way to the Internet and the big wide advertising world ever since.</p>
  <p>The advertising agency Korvanetz consists of a team of ambitious programmers, designers and marketing experts full of ideas. With us you get everything from one<br>source: from the design of classic print media on the development of logo and corporate design to the realization of your website or your online store.</p>
  <p style="margin-bottom:0">In short: work is being done here!<br>Here is looked, planned, brainstorming, thought, pondered, analyzed, organized, conceived, designed, programmed, detected, found, developed and researched.</p>
</div>
<a class="about-btn btn abs" href="#">LEARN MORE</a>

<h2 class="section-title services-title heading abs">Services</h2>

<article class="card abs" style="left:162px">
  <svg width="40" height="36" viewBox="0 0 40 36"><rect x="3" y="3" width="34" height="22" fill="none" stroke="var(--violet)" stroke-width="3"/><path d="M14 31h12M20 25v6" stroke="var(--violet)" stroke-width="3"/><path d="M15 10l-4 4 4 4M25 10l4 4-4 4M22 9l-4 10" stroke="var(--violet)" stroke-width="2" fill="none"/></svg>
  <h3>Web Development</h3>
  <p>We design and network different adver-<br>tising materials so that your advertising</p>
  <span class="more">READ MORE &gt;</span>
</article>
<article class="card abs" style="left:469px">
  <svg width="40" height="36" viewBox="0 0 40 36"><rect x="3" y="5" width="34" height="22" fill="none" stroke="var(--violet)" stroke-width="3"/><path d="M14 33h12M20 27v6" stroke="var(--violet)" stroke-width="3"/><path d="M12 22l14-14 3 3-14 14z" fill="var(--violet)"/></svg>
  <h3>Graphic Designer</h3>
  <p>We design and network different adver-<br>tising materials so that your advertising</p>
  <span class="more">READ MORE &gt;</span>
</article>
<article class="card abs" style="left:776px">
  <svg width="48" height="36" viewBox="0 0 48 36"><circle cx="28" cy="15" r="11" fill="none" stroke="var(--violet)" stroke-width="3"/><path d="M36 23l9 9" stroke="var(--violet)" stroke-width="4"/><text x="1" y="20" font-family="Poppins,sans-serif" font-weight="700" font-size="13" fill="var(--violet)">SEO</text></svg>
  <h3>Search Engine Optimization</h3>
  <p>We design and network different adver-<br>tising materials so that your advertising</p>
  <span class="more">READ MORE &gt;</span>
</article>

<svg class="shape abs over" style="top:1820px" width="1200" height="310" viewBox="0 0 1200 310">
  <path d="M0 62 C400 32 800 102 1200 252 L1200 310 L0 310 Z" fill="var(--white)"/>
  <path d="M0 50 C400 20 800 90 1200 240" stroke="var(--purple)" stroke-width="24" fill="none"/>
</svg>

<h2 class="section-title refs-title heading abs">Refrences</h2>
<p class="refs-sub abs">small excerpt of our works ...</p>
<div class="ref abs" style="left:160px;background:linear-gradient(180deg,#3a2a1e 0%,#8a5a30 45%,#f1e4cf 60%,#ffffff 100%)" role="img" aria-label="Website reference for a wine shop"></div>
<div class="ref abs" style="left:460px;background:linear-gradient(90deg,#1c1c1c 0%,#3b2a26 40%,#151515 100%)" role="img" aria-label="Website reference for a cosmetics brand"></div>
<div class="ref abs" style="left:760px;background:linear-gradient(120deg,#3a1748 0%,#5b2570 60%,#2a1035 100%)" role="img" aria-label="Website reference for a skincare product shop"></div>

<section class="contact abs bg"></section>
<svg class="shape abs bg" style="top:2880px" width="1200" height="230" viewBox="0 0 1200 230">
  <path d="M0 60 C300 160 800 200 1200 190 L1200 230 L0 230 Z" fill="var(--white)"/>
  <path d="M0 40 C260 140 700 190 1100 196" stroke="var(--blue)" stroke-width="12" fill="none" stroke-linecap="round"/>
</svg>
<h2 class="section-title contact-title heading abs">Get in Touch</h2>
<form class="form-card abs">
  <div class="field abs" style="top:46px">First Name</div>
  <div class="field abs" style="top:90px">Last Name</div>
  <div class="field abs" style="top:132px">Job Title</div>
  <div class="field abs" style="top:176px">Company</div>
  <div class="field abs" style="top:220px">Email</div>
  <div class="field abs" style="top:264px">Phone</div>
  <a class="submit btn abs" href="#">SUBMIT</a>
</form>

<footer class="footer abs">
  <span>© Copyright &nbsp;2018 Korvanetz.de</span>
  <div class="social abs"><span></span><span></span><span></span><span></span><span></span><span></span></div>
  <a class="support btn abs" href="#">Quick Support</a>
</footer>

</body>
</html>
```